Need modern simple design for magazine ad, apartment and condo roofer.

I need a half page magazine ad for a local roofer to publish in an industry magazine. Apartment associations industry. All types of roofs. Shingle and Flat
Need the design to be creative and modern, clean and simple. I do not want a busy design. One that stands out and makes a point quickly.
Logo must be prominent.
DO NOT USE PHOTOS FROM MY WEBSITE PLEASE. Looking for something new.
I work on entire complexes not houses.

Need to make sure our phone number and email address are listed at the bottom. Here is my website www.vorbelan.com
Want to stay away from standard clip arts of tools, homes, apartment buildings.
Half Horizontal 7.25 x 4.75
Ads should be in PDF and JPG format.

Target Market(s)

Apartment or Condo owners looking for large scale roofing projects

Industry/Entity Type

Roofing

Requirements
Must have
• Prominent Logo
Simple Clean Design
Create graphics
Not Busy
Should not have
• Clip Art
No Photos from my website

```html
<!DOCTYPE html>
<html lang="en">
<head>
<meta charset="utf-8">
<title>Vorbelan Roofing – Half Page Ad</title>
<link rel="stylesheet" href="https://fonts.googleapis.com/css2?family=League+Gothic&display=swap">
<style>
  :root {
    --page: #ffffff;
    --brand-blue: #2a6aae;
    --tan: #dba25e;
    --panel-grey: #d0cfd0;
    --ink: #262626;
    --white: #ffffff;
  }
  * { margin: 0; padding: 0; box-sizing: border-box; }
  html, body { width: 1200px; height: 866px; overflow: hidden; background: var(--page); }
  body { position: relative; font-family: "League Gothic", "Arial Narrow", sans-serif; }

  .ad {
    position: absolute; left: 88px; top: 98px;
    width: 1023px; height: 669px;
    background: var(--white); overflow: hidden;
  }
  .ad__bg { position: absolute; inset: 0; }

  .brand {
    position: absolute; left: 37px; top: 52px;
    display: flex; align-items: center; gap: 16px;
  }
  .brand__mark { width: 62px; height: 62px; background: var(--brand-blue); flex: none; }
  .brand__name {
    font-size: 76px; line-height: 1; color: var(--brand-blue);
    letter-spacing: 1px; text-transform: uppercase; white-space: nowrap;
  }

  .headline {
    position: absolute; left: 37px; top: 190px;
    color: var(--white); font-weight: 400; text-transform: uppercase;
    font-size: 130px; line-height: 94px;
    transform: scaleX(0.78); transform-origin: left top;
    white-space: nowrap;
  }
  .headline span { display: block; }

  .tagline {
    position: absolute; left: 27px; top: 480px;
    width: 377px; height: 58px;
    background: var(--tan); color: var(--ink);
    font-size: 43px; line-height: 58px; padding-left: 9px;
    white-space: nowrap; overflow: hidden;
  }
  .tagline span { display: inline-block; transform: scaleX(0.92); transform-origin: left center; }

  .contact__icon { position: absolute; width: 30px; height: 30px; }
  .contact__text {
    position: absolute; color: var(--ink); line-height: 1;
    white-space: nowrap; transform-origin: left top;
  }
  .icon--address { left: 449px; top: 559px; }
  .icon--phone   { left: 449px; top: 609px; }
  .icon--email   { left: 659px; top: 609px; }
  .text--address { left: 490px; top: 556px; font-size: 37px; transform: scaleX(0.94); }
  .text--phone   { left: 490px; top: 600px; font-size: 50px; transform: scaleX(0.84); }
  .text--email   { left: 704px; top: 600px; font-size: 50px; }
</style>
</head>
<body>
  <section class="ad">
    <svg class="ad__bg" width="1023" height="669" viewBox="0 0 1023 669">
      <defs>
        <linearGradient id="scene-tone" x1="0" y1="0" x2="0" y2="1">
          <stop offset="0" stop-color="#9a9a9a"/>
          <stop offset="0.38" stop-color="#7d7d7d"/>
          <stop offset="0.5" stop-color="#b07a3e"/>
          <stop offset="0.75" stop-color="#9c7a4c"/>
          <stop offset="1" stop-color="#c98a45"/>
        </linearGradient>
        <linearGradient id="scene-fade" x1="0" y1="0" x2="1" y2="0">
          <stop offset="0" stop-color="#ffffff" stop-opacity="1"/>
          <stop offset="1" stop-color="#ffffff" stop-opacity="0"/>
        </linearGradient>
      </defs>
      <rect x="0" y="0" width="1023" height="669" fill="var(--panel-grey)"/>
      <rect x="0" y="0" width="1023" height="170" fill="var(--white)"/>
      <g role="img" aria-label="Photograph of a historic building with terracotta tile roofs and a bell tower before a mountain lake">
        <polygon points="420,0 1023,0 1023,527 436,547 436,170 420,170" fill="url(#scene-tone)"/>
        <rect x="400" y="0" width="220" height="260" fill="url(#scene-fade)"/>
      </g>
      <polygon points="0,170 436,170 436,547 0,669" fill="var(--brand-blue)"/>
    </svg>

    <div class="brand">
      <div class="brand__mark"></div>
      <div class="brand__name">Vorbelan Roofing</div>
    </div>

    <h1 class="headline">
      <span>Apartment</span>
      <span>Associations</span>
      <span>Industry</span>
    </h1>

    <p class="tagline"><span>All types of roofs. Shingle And Flat</span></p>

    <svg class="contact__icon icon--address" viewBox="0 0 30 30" aria-hidden="true">
      <circle cx="15" cy="15" r="15" fill="var(--tan)"/>
      <path d="M15 7a5 5 0 0 0-5 5c0 4 5 9 5 9s5-5 5-9a5 5 0 0 0-5-5z" fill="none" stroke="var(--brand-blue)" stroke-width="2"/>
      <circle cx="15" cy="12" r="1.8" fill="var(--brand-blue)"/>
      <path d="M9 23h12" stroke="var(--brand-blue)" stroke-width="2"/>
    </svg>
    <p class="contact__text text--address">214 Harlow Avenue, Suite 120 Millbrook, TX 75061</p>

    <svg class="contact__icon icon--phone" viewBox="0 0 30 30" aria-hidden="true">
      <circle cx="15" cy="15" r="15" fill="var(--tan)"/>
      <rect x="10.5" y="6.5" width="9" height="17" rx="1.5" fill="none" stroke="var(--brand-blue)" stroke-width="2"/>
      <circle cx="15" cy="20.5" r="1" fill="var(--brand-blue)"/>
    </svg>
    <p class="contact__text text--phone">555.014.2290</p>

    <svg class="contact__icon icon--email" viewBox="0 0 30 30" aria-hidden="true">
      <circle cx="15" cy="15" r="15" fill="var(--tan)"/>
      <rect x="7.5" y="10" width="15" height="10" fill="var(--brand-blue)"/>
      <path d="M7.5 10l7.5 6 7.5-6" fill="none" stroke="var(--tan)" stroke-width="1.4"/>
    </svg>
    <p class="contact__text text--email">info@vorbelan.com</p>
  </section>
</body>
</html>
```